Poem Handwritten by Veteran while in the jungle of Vietnam

My parents are celebrating their 50th wedding anniversary this year. I wanted to give them a very memorable gift. On my parents 2nd anniversary, my father was stationed in Vietnam. On that night he was in the jungle waiting till morning and wrote a poem to my mother using his pant leg as paper. I would like this poem to typographically designed to be framed and hung on the wall.

I have attached a picture of the poem below. It will need to be 11x14 when printed for framing. It would be great if there was background or artwork to make it more visually interesting, perhaps in a watercolor. My parents have a transitional style. I have attached some possible color schemes as well. Cool greens, blue, neutral grays, with hints of berries or highlights of yellow. These are just a guide, I would be open to your interpretations.

Thank you for your help. This will hopefully be a gift they will truly treasure as much as the poem itself.

Target Market(s)

My parents who are excited to be celebrating their 50th wedding anniversary. It should have a transitional, mature style.

Font styles to use
Serif
Script

Requirements
Must have
• The poem, typographically designed. There can be a mix of fonts, but legibility is critically important.
• Now that some designs have come through I wanted to give some more guidance of what I'm looking for. I want something that feels sophisticated and artistic.
Nice to have
• A background or art work, using the color schemes attached as a guide. I am really liking the designs that have a full color landscape artwork in the background. The fonts should be elegant and formal. I really like the romantic, muted colors. I had trouble finding similar projects online in the style I wanted until I cam across wedding invites. Those seem to be the most applicable. I've added pictures of some so you can get a sense of what I'm looking for. I am really liking the jungle foliage, starry skies or sunrises.
Should not have
• Cartoon caricatures, fonts that are too illegible when printed. I'm not liking anything whimsical. I don't like the very bright colors for this project.

```html
<!DOCTYPE html>
<html lang="en">
<head>
<meta charset="utf-8">
<title>Walter's Anniversary Poem</title>
<link href="https://fonts.googleapis.com/css2?family=Allura&family=Cormorant+Garamond:wght@500&family=Old+Standard+TT&family=Montserrat:wght@400&display=swap" rel="stylesheet">
<style>
  :root {
    --canvas: #ececec;
    --mint: #bcdcc9;
    --mint-soft: #d3e6d8;
    --cream: #ebe8e1;
    --blush: #e6c6d2;
    --leaf: #a9bf95;
    --title-green: #5f8863;
    --verse-green: #4f7a58;
    --berry: #c48d9c;
    --panel: rgba(255, 255, 255, 0.72);
    --note-grey: #9a9f9b;
  }
  * { margin: 0; padding: 0; box-sizing: border-box; }
  html, body {
    width: 1200px; height: 1200px; overflow: hidden;
    background: var(--canvas);
  }
  .poster {
    position: absolute;
    left: 208px; top: 30px;
    width: 784px; height: 1140px;
    overflow: hidden;
  }
  .poster__artwork {
    position: absolute; inset: 0;
    background: linear-gradient(180deg,
      var(--mint) 0%, var(--mint-soft) 30%, #dfe6d6 52%,
      #e9dfe2 72%, var(--blush) 86%, #dcdcc6 100%);
  }
  .verse-panel {
    position: absolute;
    left: 202px; top: 57px;
    width: 390px; height: 1005px;
    background: var(--panel);
    box-shadow: 0 2px 10px rgba(60, 90, 70, 0.18);
  }
  .title { position: absolute; left: 0; width: 100%; text-align: center; }
  .title__name {
    top: 93px;
    font-family: "Cormorant Garamond", serif;
    font-weight: 500;
    font-size: 46px; letter-spacing: 3px;
    color: var(--berry);
  }
  .title__script {
    top: 122px; left: 6px;
    font-family: "Allura", cursive;
    font-size: 150px; line-height: 1;
    color: var(--title-green);
  }
  .title__poem {
    top: 234px;
    font-family: "Cormorant Garamond", serif;
    font-weight: 500;
    font-size: 48px; letter-spacing: 3px;
    color: var(--title-green);
  }
  .dateline {
    position: absolute; top: 296px; left: 0; width: 100%;
    text-align: center;
    font-family: "Old Standard TT", serif;
    font-size: 16.5px;
    color: var(--berry);
  }
  .poem {
    position: absolute; top: 326px; left: 202px; width: 390px;
    text-align: center;
    font-family: "Old Standard TT", serif;
    font-size: 11.6px; line-height: 12.27px;
    color: var(--verse-green);
  }
  .poem__stanza + .poem__stanza { margin-top: 12.27px; }
  .poem__line { display: block; white-space: nowrap; }
  .footnote {
    position: absolute; top: 1010px; left: 228px; width: 338px;
    text-align: center;
    font-family: "Montserrat", sans-serif;
    font-size: 6.4px; line-height: 8.6px;
    color: var(--note-grey);
  }
</style>
</head>
<body>
  <main class="poster">
    <div class="poster__artwork" role="img" aria-label="Watercolour background of soft mint wash with pink peonies, berries and green leafy sprigs"></div>
    <div class="verse-panel"></div>

    <h1>
      <span class="title title__name">WALTER’S</span>
      <span class="title title__script">Anniversary</span>
      <span class="title title__poem">POEM</span>
    </h1>
    <p class="dateline">20 July 1970, Monday, LZ Meridian</p>

    <article class="poem">
      <p class="poem__stanza">
        <span class="poem__line">Life’s journey began with a challenge,</span>
        <span class="poem__line">It was heralded far and near.</span>
        <span class="poem__line">The road led on forever,</span>
        <span class="poem__line">Its completion was known to be dear.</span>
      </p>
      <p class="poem__stanza">
        <span class="poem__line">From the garden of light it proceeded,</span>
        <span class="poem__line">To the valley of shadows it led.</span>
        <span class="poem__line">Thorns and thistles adorned it,</span>
        <span class="poem__line">Past abyss and crevice it sped.</span>
      </p>
      <p class="poem__stanza">
        <span class="poem__line">The brave surged forward with courage,</span>
        <span class="poem__line">The wise undaunted pressed on.</span>
        <span class="poem__line">The mighty held high their banner,</span>
        <span class="poem__line">We all awaited the dawn.</span>
      </p>
      <p class="poem__stanza">
        <span class="poem__line">Though the pitfalls and hazards were many,</span>
        <span class="poem__line">The pathway was clearly in view.</span>
        <span class="poem__line">Straight and sure it glided,</span>
        <span class="poem__line">Its course we knew to be true.</span>
      </p>
      <p class="poem__stanza">
        <span class="poem__line">I knew you, Sweetheart, beforehand,</span>
        <span class="poem__line">So precious and sweet were you,</span>
        <span class="poem__line">Our moments of bliss were priceless,</span>
        <span class="poem__line">Each day brought us joy anew.</span>
      </p>
      <p class="poem__stanza">
        <span class="poem__line">The call to progression beckoned,</span>
        <span class="poem__line">At last I would have my chance –</span>
        <span class="poem__line">To clasp you to me forever,</span>
        <span class="poem__line">And seal our divine romance.</span>
      </p>
      <p class="poem__stanza">
        <span class="poem__line">I eagerly started the journey,</span>
        <span class="poem__line">Though with sorrow, I left you behind.</span>
        <span class="poem__line">With courage and faith I continued,</span>
        <span class="poem__line">For I knew, that you later I’d find.</span>
      </p>
      <p class="poem__stanza">
        <span class="poem__line">I diligently searched for you, Darling,</span>
        <span class="poem__line">The roadway was both bleak and fair.</span>
        <span class="poem__line">Though the years grew long in number,</span>
        <span class="poem__line">I did not give up in despair.</span>
      </p>
      <p class="poem__stanza">
        <span class="poem__line">At last in the distance I saw you,</span>
        <span class="poem__line">So beautiful, lovely, and sweet!</span>
        <span class="poem__line">Your attention I struggled to capture,</span>
        <span class="poem__line">Your love I wrested to meet.</span>
      </p>
      <p class="poem__stanza">
        <span class="poem__line">What rapture was mine in fulfillment,</span>
        <span class="poem__line">As now together we stand.</span>
        <span class="poem__line">To cherish and love each other,</span>
        <span class="poem__line">While our plans and dreams expand.</span>
      </p>
      <p class="poem__stanza">
        <span class="poem__line">I love you, Darling, forever,</span>
        <span class="poem__line">My life you have made replete.</span>
        <span class="poem__line">Our eternal mansion beckons</span>
        <span class="poem__line">Your love has made it complete.</span>
      </p>
    </article>

    <p class="footnote">This poem was written during the dark of night while on guard duty at LZ Meridian in Viet Nam. I was at the time a 2nd Lieutenant in the Infantry. The date was July, 1970, our second anniversary. The original was penciled onto my army uniform, arranging only the key rhyming words without light to see.</p>
  </main>
</body>
</html>
```